Postcard: Open Sky Circle

Text for front: HOW TO CHANGE THE WORLD IN ONE [note: the word "one" should be underlined] STEPHint: It's up to you...[Note: add arrow or something to indicate "turn over"]Text for back: You're going to spend your entire life with someone you can never get away from. (Guess who?) Wouldn't you rather that person #OpenSkyCircle than judgmental or critical? BE the change you want to see! Visit www.OpenSkyCircle-hub.example for daily Dawn Pebbles and community. PLEASE JOIN US![Note: add logo to left half of back side]Font preference for text: Josefin sans

Target Market(s)

People who would be attracted to Corvane church - teravian perennist message. It's spiritual without being overtly religious, so the target market is probably early 30s and up but ideally won't turn off Millennials (folks under 30). It should attract attention of people who are open-minded and committed to progressive social change, tired of an atmosphere of hate-mongering and divisiveness.

Requirements
Nice to have
• It would be nice to convey a sense of challenge - there is an idea of "dawn pebbles" so something related to fire/sparks is appropriate. This is meant to evoke a deeper, divine love more than a sense of romantic love. This love is more fierce than fluffy! Yet it calls us to be our best selves.
Should not have
• Please avoid excessive pink - just the logo is enough, as this design needs to appeal to men as well as women.

```html
<!DOCTYPE html>
<html lang="en">
<head>
<meta charset="utf-8">
<title>Open Sky Circle Postcard</title>
<link rel="stylesheet" href="https://fonts.googleapis.com/css2?family=Josefin+Sans:wght@300;400;600;700&family=Pinyon+Script&display=swap">
<style>
  :root {
    --backdrop: #262626;
    --violet-deep: #2a1a8a;
    --violet: #5b3fd6;
    --blue-glow: #4a7bf0;
    --teal-core: #5fb3c9;
    --panel-tint: rgba(150, 140, 230, 0.28);
    --white: #ffffff;
    --ink: #1e1c1d;
    --back-dark: #231f20;
    --band-grey: #e4e4e4;
    --logo-rose: #e0567a;
  }
  * { box-sizing: border-box; margin: 0; padding: 0; }
  html, body { width: 900px; height: 1200px; overflow: hidden; }
  body {
    position: relative;
    background: var(--backdrop);
    font-family: "Josefin Sans", sans-serif;
  }

  /* ---------- Front side ---------- */
  .card-front {
    position: absolute;
    left: 107px; top: 85px;
    width: 713px; height: 475px;
    overflow: hidden;
  }
  .front-artwork {
    position: absolute; inset: 0;
    background:
      radial-gradient(ellipse 30% 40% at 50% 48%, var(--teal-core) 0%, rgba(95,179,201,0) 70%),
      radial-gradient(ellipse 60% 70% at 50% 50%, var(--blue-glow) 0%, var(--violet) 55%, var(--violet-deep) 100%);
  }
  .title-panel {
    position: absolute;
    left: 58px; top: 77px;
    width: 592px; height: 271px;
    background: var(--panel-tint);
  }
  .title {
    position: absolute;
    left: 58px; top: 96px;
    width: 592px;
    text-align: center;
    color: var(--white);
    white-space: nowrap;
  }
  .title-lead {
    display: block;
    font-weight: 600;
    font-size: 58px;
    line-height: 60px;
    letter-spacing: 0.5px;
  }
  .title-main {
    display: block;
    font-weight: 300;
    font-size: 94px;
    line-height: 86px;
    margin-top: 12px;
  }
  .title-main + .title-main {
    margin-top: 0;
    font-size: 92px;
    letter-spacing: -2px;
  }
  .title-main u {
    text-decoration-thickness: 3px;
    text-underline-offset: 6px;
  }
  .turn-arrow {
    position: absolute;
    left: 540px; top: 318px;
  }
  .hint {
    position: absolute;
    left: 0; right: 0; top: 380px;
    text-align: center;
    color: var(--white);
    font-family: "Pinyon Script", cursive;
    font-size: 46px;
    line-height: 1;
    white-space: nowrap;
  }
  .hint strong { font-size: 56px; font-weight: 400; }
  .hint-rule {
    position: absolute;
    left: 45px; top: 441px;
    width: 623px; height: 2px;
    background: var(--white);
  }

  /* ---------- Back side ---------- */
  .card-back {
    position: absolute;
    left: 107px; top: 642px;
    width: 713px; height: 476px;
    background: var(--back-dark);
    overflow: hidden;
  }
  .logo-panel {
    position: absolute;
    left: 0; top: 0;
    width: 355px; height: 338px;
    background: var(--white);
    display: flex;
    flex-direction: column;
    align-items: center;
    justify-content: center;
    gap: 22px;
  }
  .logo-mark {
    width: 40px; height: 40px;
    border-radius: 50%;
    background: var(--logo-rose);
  }
  .logo-name {
    font-weight: 400;
    font-size: 30px;
    letter-spacing: 3px;
    color: var(--logo-rose);
    text-transform: uppercase;
    text-align: center;
    line-height: 1.2;
  }
  .message {
    position: absolute;
    left: 371px; top: 34px;
    width: 327px;
    color: var(--white);
    font-weight: 400;
    font-size: 18px;
    line-height: 27px;
    text-align: justify;
  }
  .message p + p { margin-top: 24px; text-align: left; }
  .message strong { font-weight: 700; }
  .web-address {
    display: inline-block;
    background: var(--white);
    color: var(--ink);
    font-size: 16px;
    font-weight: 600;
    padding: 3px 6px 0;
    line-height: 22px;
    margin: 2px 0;
    white-space: nowrap;
  }
  .join-band {
    position: absolute;
    left: 0; top: 338px;
    width: 713px; height: 97px;
    background: var(--band-grey);
    display: flex;
    align-items: center;
    justify-content: center;
    color: var(--ink);
    font-weight: 300;
    font-size: 58px;
    letter-spacing: 1px;
    padding-top: 8px;
    white-space: nowrap;
  }
  .test-note {
    position: absolute;
    left: 0; top: 435px;
    width: 355px; height: 41px;
    background: var(--white);
    color: var(--ink);
    font-size: 14px;
    padding: 14px 0 0 14px;
    white-space: nowrap;
  }
</style>
</head>
<body>

  <section class="card-front">
    <div class="front-artwork" role="img" aria-label="Silhouette of a person meditating cross-legged amid radiating violet and blue energy rays"></div>
    <div class="title-panel"></div>
    <h1 class="title">
      <span class="title-lead">HOW TO CHANGE</span>
      <span class="title-main">THE WORLD</span>
      <span class="title-main">IN <u>ONE</u> STEP</span>
    </h1>
    <svg class="turn-arrow" width="175" height="70" viewBox="0 0 175 70" aria-hidden="true">
      <path d="M8 22 C 40 70, 120 70, 150 24" fill="none" stroke="#ffffff" stroke-width="8" stroke-linecap="round"/>
      <path d="M130 22 L165 6 L158 44 Z" fill="#ffffff"/>
    </svg>
    <p class="hint"><strong>Hint:</strong> It's up to you...</p>
    <div class="hint-rule"></div>
  </section>

  <section class="card-back">
    <div class="logo-panel">
      <div class="logo-mark"></div>
      <div class="logo-name">Open Sky<br>Circle</div>
    </div>
    <div class="message">
      <p>You're going to spend your entire life with someone you can never get away from. (Guess who?) Wouldn't you rather that person #OpenSkyCircle than judgmental or critical?</p>
      <p><strong>BE</strong> the change you want to see!<br>Visit <span class="web-address">www.OpenSkyCircle-hub.example</span><br>for daily Dawn Pebbles and community.</p>
    </div>
    <div class="join-band">PLEASE JOIN US!</div>
    <div class="test-note">A/B test:How to change/the world/your life</div>
  </section>

</body>
</html>
```